Board to put on a meditation centre - Lantern Grove

I need a board design for a new meditation centre based in Oslo which offers free courses in meditation and self-empowerment. The size of the board is width 374cm x height 104cm.  The name of the meditation centre together with subtitles should be on the board but also some elegant decoration that matches the theme (lantern grove/meditation).
Here is the website of the meditation centre to give you a feeling of it: https://lyktelundsenteret.no/
Good if you can use a blue color close to this one: rgb(37, 180, 193) as well as some brown/golden color (similar to the palette on the website).
On the board it should say:
Lyktelunden (in big letters, the rest is subtitles)
Meditasjon & Spirituell visdom
Kurs - Retreat - Dialog
lyktelundsenteret.no
The design should be very elegant and beautiful and the feeling should be of "An Lantern Grove". A logo is here attached and should be used but I need to get a better quality version of it, will upload that as soon as possible.

```html
<!DOCTYPE html>
<html lang="no">
<head>
<meta charset="utf-8">
<title>Lyktelunden – skiltforslag</title>
<link href="https://fonts.googleapis.com/css2?family=Marcellus&family=Josefin+Sans:wght@300&family=Quicksand:wght@500&display=swap" rel="stylesheet">
<style>
  :root{
    --page:#ffffff;
    --frame-sky:#bcdee7;
    --panel-light:#eaf4fb;
    --panel-mid:#c9e4ee;
    --mist-a:#cfe9ec;
    --mist-b:#a9d8d2;
    --teal:#25b4c1;
    --teal-band:#24adba;
    --teal-title:#1f98a3;
    --ink:#14181a;
    --gold-dark:#bf8a2b;
    --gold-light:#e9d391;
    --brand-red:#d52b2f;
    --white:#ffffff;
  }
  *{margin:0;padding:0;box-sizing:border-box}
  html,body{width:1200px;height:840px;overflow:hidden;background:var(--page)}
  .canvas{position:relative;width:1200px;height:840px}

  .board{position:absolute;left:var(--x);top:var(--y);width:997px;height:277px}
  .board--pattern{--x:101px;--y:110px;background:var(--frame-sky)}
  .board--mist{--x:95px;--y:473px}
  .mist-bg{position:absolute;inset:0;background:linear-gradient(115deg,var(--mist-b) 0%,var(--mist-a) 40%,#d7eef0 70%,var(--mist-b) 100%)}

  .panel{position:absolute;box-shadow:0 0 6px rgba(40,90,110,.25)}
  .board--pattern .panel{left:22px;top:23px;width:953px;height:197px;
    background:linear-gradient(180deg,var(--panel-light) 0%,var(--panel-mid) 100%)}
  .board--mist .panel{left:23px;top:18px;width:952px;height:203px;
    background:linear-gradient(160deg,#e0eff7 0%,#cfe8ea 60%,#c3e3e3 100%)}

  .gold-rule{position:absolute;left:0;width:100%;height:6px;
    background:linear-gradient(90deg,var(--gold-dark) 0%,var(--gold-light) 35%,var(--gold-dark) 60%,var(--gold-light) 85%,var(--gold-dark) 100%)}
  .base-band{position:absolute;left:0;width:100%;background:var(--teal-band)}
  .board--pattern .gold-rule{top:220px}
  .board--pattern .base-band{top:226px;height:51px}
  .board--mist .gold-rule{top:221px}
  .board--mist .base-band{top:227px;height:50px}

  .web{position:absolute;font-family:"Quicksand",sans-serif;font-weight:500;color:var(--white);font-size:16px;letter-spacing:.3px;line-height:1}

  .brand{position:absolute;display:flex;flex-direction:column;align-items:center;gap:8px;width:120px}
  .brand__dot{width:46px;height:46px;border-radius:50%;background:var(--brand-red)}
  .brand__name{font-family:"Quicksand",sans-serif;font-weight:500;font-size:15px;color:var(--brand-red);line-height:1}

  .title{position:absolute;white-space:nowrap;color:var(--teal-title);line-height:1;transform:translateX(-50%)}
  .title--serif{font-family:"Marcellus",serif;font-size:84px}
  .title--sans{font-family:"Josefin Sans",sans-serif;font-weight:300;font-size:76px;letter-spacing:1px}

  .tagline{position:absolute;white-space:nowrap;font-family:"Quicksand",sans-serif;font-weight:500;color:var(--ink);line-height:1}

  .offer{position:absolute;display:flex;align-items:center;font-family:"Quicksand",sans-serif;font-weight:500;line-height:1;list-style:none}
  .offer li{display:flex;align-items:center;gap:7px;white-space:nowrap}
  .offer .mark{display:inline-block;width:22px;height:3px;border-radius:2px;background:linear-gradient(90deg,var(--gold-dark),var(--gold-light))}
  .offer--plain{font-size:19px;color:var(--ink)}
  .offer--plain li{margin-right:24px}
  .offer--bar{left:281px;top:186px;width:578px;height:35px;background:var(--teal);color:var(--white);font-size:18px;letter-spacing:9px;padding-left:55px}
  .offer--bar li{position:absolute}
  .offer--bar .mark{width:20px}
</style>
</head>
<body>
<main class="canvas">

  <section class="board board--pattern" aria-label="Skiltforslag 1">
    <div class="panel" role="img" aria-label="Lyst blått felt med dekorativt bladmønster"></div>
    <div class="brand" style="left:70px;top:86px">
      <span class="brand__dot"></span>
      <span class="brand__name">Lyktelunden</span>
    </div>
    <h1 class="title title--serif" style="left:574px;top:52px">LYKTELUNDEN</h1>
    <p class="tagline" style="left:392px;top:144px;font-size:28px">Meditasjon &amp; Spirituell visdom</p>
    <ul class="offer offer--plain" style="left:460px;top:190px">
      <li><span class="mark"></span>Kurs</li>
      <li><span class="mark"></span>Retreat</li>
      <li><span class="mark"></span>Dialog</li>
    </ul>
    <div class="gold-rule"></div>
    <div class="base-band" role="img" aria-label="Turkis bånd med bladmønster"></div>
    <p class="web" style="left:691px;top:232px">lyktelundsenteret.no</p>
  </section>

  <section class="board board--mist" aria-label="Skiltforslag 2">
    <div class="mist-bg" role="img" aria-label="Mykt akvarellaktig bakgrunn i mintgrønt"></div>
    <div class="panel"></div>
    <div class="brand" style="left:25px;top:96px">
      <span class="brand__dot"></span>
      <span class="brand__name">Lyktelunden</span>
    </div>
    <h1 class="title title--sans" style="left:560px;top:62px">LYKTELUNDEN</h1>
    <p class="tagline" style="left:457px;top:133px;font-size:30px">Meditasjon &amp; Spirituell visdom</p>
    <ul class="offer offer--bar">
      <li style="left:40px"><span class="mark"></span>KURS</li>
      <li style="left:178px"><span class="mark"></span>RETREAT</li>
      <li style="left:400px"><span class="mark"></span>DIALOG</li>
    </ul>
    <div class="gold-rule"></div>
    <div class="base-band"></div>
    <p class="web" style="left:782px;top:241px">lyktelundsenteret.no</p>
  </section>

</main>
</body>
</html>
```